Business card design needed

the business is HR Consulting, but its for SME businesses who cant afford a permanent HR person. We sell an HR info system to help them meet minimum employment legislation but with this hope they then require us on a monthly subscription to phone or email us for HR advice. We are HR qualified mums working from home

So we will be partners to HR and Payroll systems known as kindle HR and Pluto

Target Market(s)

Small to medium businesses so not black and overly corporate, but having said that many are accounting businesses

Industry/Entity Type

Business

Contact Information for Business Card

Name of the company: Quillmere HR

Me:Marta Kovalenko
Title:Managing Director

m: 0437 215 683
e: marta@quillmerehr.com.au
w: www.quillmerehr.com.au

What we do: HR Consulting, HR Systems and support, Payroll Advice

Requirements
Nice to have
• there is a company already out there known as Quartz professionals. I like the leaves at the end as I wanted something different like this to the usual business logos but still professional. I wanted a symbol to show calm, positive, ease flow going up ,etc. but realise they have the leaves and possibly cant copy, or can we?..( kite??, something calm and positive)dont know!!. Green and blue needed to be in it as nature and calm as well. I love the colours of www.stafflanefund.com ( attached the colours), as well as the calm wave line underneath. have a look as while they use green and blue I loved the purple colour thrown in there.Green and blue on their own are so overused. I want vibrant. I want double sided and when on a table I want it to stand out so maybe the purple colour (as per the colours on the fund website) solid on one side with just the 3 services we provide and personal and company name on front but need some creativity from you guys.

```html
<!DOCTYPE html>
<html lang="en">
<head>
<meta charset="utf-8">
<title>Quillmere HR – Business Card Options</title>
<link rel="stylesheet" href="https://fonts.googleapis.com/css2?family=PT+Sans:wght@400;700&display=swap">
<style>
  :root {
    --page-bg: #ffffff;
    --card-bg: #ffffff;
    --card-frame: #555555;
    --brand-grey: #808080;
    --name-grey: #7d7d7d;
    --title-grey: #b8b8b8;
    --body-grey: #666666;
    --accent-purple: #a3157a;
  }
  * { box-sizing: border-box; margin: 0; padding: 0; }
  html, body {
    width: 1200px;
    height: 904px;
    overflow: hidden;
    background: var(--page-bg);
  }
  body {
    position: relative;
    font-family: "PT Sans", "Trebuchet MS", sans-serif;
  }
  .card {
    position: absolute;
    top: 0;
    width: 574px;
    height: 904px;
    background: var(--card-bg);
    border: 13px solid var(--card-frame);
    text-align: center;
  }
  .card--option-a { left: 22px; }
  .card--option-b { left: 618px; }

  .brand {
    position: absolute;
    top: 166px;
    left: 0;
    right: 0;
    display: flex;
    align-items: center;
    justify-content: center;
    gap: 18px;
  }
  .brand__name {
    font-size: 66px;
    font-weight: 400;
    color: var(--brand-grey);
    line-height: 1;
    letter-spacing: 0.5px;
    white-space: nowrap;
  }
  .brand__dot {
    flex: none;
    width: 46px;
    height: 46px;
    border-radius: 50%;
    background: var(--accent-purple);
  }

  .person {
    position: absolute;
    top: 418px;
    left: 0;
    right: 0;
  }
  .person__name {
    font-size: 42px;
    font-weight: 400;
    color: var(--name-grey);
    line-height: 1.1;
    letter-spacing: 0.5px;
  }
  .person__title {
    margin-top: 0;
    font-size: 19px;
    line-height: 1.2;
    color: var(--title-grey);
    letter-spacing: 0.8px;
    text-transform: uppercase;
  }
  .person__contact {
    margin-top: 14px;
    font-size: 20px;
    line-height: 1.2;
    color: var(--body-grey);
    white-space: nowrap;
  }

  .footer {
    position: absolute;
    bottom: 38px;
    left: 0;
    right: 0;
    color: var(--body-grey);
  }
  .footer__web {
    font-size: 21px;
    letter-spacing: 0.5px;
  }
  .footer__services {
    margin-top: 4px;
    font-size: 22px;
    white-space: nowrap;
  }
</style>
</head>
<body>
  <section class="card card--option-a" aria-label="Business card option A">
    <div class="brand">
      <span class="brand__name">Quillmere HR</span>
      <span class="brand__dot" aria-hidden="true"></span>
    </div>
    <div class="person">
      <h1 class="person__name">Marta Kovalenko</h1>
      <p class="person__title">Managing Director</p>
      <p class="person__contact">0437 215 683 || marta@quillmerehr.com.au</p>
    </div>
    <div class="footer">
      <p class="footer__web">www.quillmerehr.com.au</p>
      <p class="footer__services">HR Consulting || HR Strategy || HR Systems Support</p>
    </div>
  </section>

  <section class="card card--option-b" aria-label="Business card option B">
    <div class="brand">
      <span class="brand__name">Quillmere HR</span>
      <span class="brand__dot" aria-hidden="true"></span>
    </div>
    <div class="person">
      <h2 class="person__name">Marta Kovalenko</h2>
      <p class="person__title">Managing Director</p>
      <p class="person__contact">0437 215 683 || marta@quillmerehr.com.au</p>
    </div>
    <div class="footer">
      <p class="footer__web">www.quillmerehr.com.au</p>
      <p class="footer__services">HR Consulting || HR Strategy || HR Systems Support</p>
    </div>
  </section>
</body>
</html>
```